CopperWren Works, LLC Corporate Web Site

The goal of this web site is simple. To provide an information and corporate information site for people who click on company links from other web sites. Put simply, this web site is primarily a brochure web site for the parent business. It will contain information about the company and our products with links to those products. It will be designed as a small web site but scalable as we add more products and services to our repertoire.

Please see the PDF in the uploaded files/media for more information on colors and basic guidelines, but be creative for sure.

Target Market(s)

General

Industry/Entity Type

Technology, Software

Coding

Coded - Design and coding required

Font styles to use
Other font styles liked:
• Goliath, Roboto

Colors
FFC000
F8CF3A
FAE287
FDF2CF
FEFAEE

Requirements
Must have
• Home page template, interior template, News/Press release template
Nice to have
• Searchable
Should not have
• carousels, one-page design

```html
<!DOCTYPE html>
<html lang="en">
<head>
<meta charset="utf-8">
<title>CopperWren Works</title>
<link href="https://fonts.googleapis.com/css2?family=Poppins:wght@400;500;600;700&display=swap" rel="stylesheet">
<style>
:root{
  --orange:#ff8a00;
  --ink:#1d1d1d;
  --grey-card:#e6e6e6;
  --contact-bg:#f4f2f2;
  --white:#ffffff;
  --line-blue:#4a5fc1;
}
*{margin:0;padding:0;box-sizing:border-box}
html,body{width:1200px;height:3514px;overflow:hidden}
body{font-family:'Poppins',sans-serif;color:var(--ink);background:var(--white);position:relative}
.abs{position:absolute}
/* header */
.site-header{left:0;top:0;width:1200px;height:130px;background:#f7f7f7}
.brand{left:87px;top:40px;font-size:34px;font-weight:700;color:var(--orange);display:flex;align-items:center;gap:10px;line-height:48px}
.brand .dot{width:12px;height:12px;border-radius:50%;background:var(--orange)}
.nav{left:475px;top:56px;display:flex;gap:20px;font-size:15px;font-weight:500}
.nav a{color:var(--ink);text-decoration:none;padding-bottom:6px}
.nav a.active{color:var(--orange);border-bottom:2px solid var(--orange)}
/* hero */
.hero{left:0;top:130px;width:1200px;height:583px;background:linear-gradient(180deg,#4a4c50 0%,#3a3b3e 55%,#232325 100%)}
.hero-title{left:0;top:246px;width:1200px;text-align:center;color:var(--white);font-size:42px;font-weight:700;line-height:50px}
.hero-text{left:300px;top:378px;width:600px;text-align:center;color:var(--white);font-size:21px;line-height:29px}
.btn-outline{border:2px solid var(--white);color:var(--white);font-size:21px;font-weight:500;display:flex;align-items:center;justify-content:center}
.hero-btn{left:520px;top:519px;width:162px;height:42px;border-radius:4px}
/* products */
.section-title{color:var(--orange);font-weight:700}
.products-title{left:0;top:762px;width:1200px;text-align:center;font-size:40px}
.card{top:874px;width:313px;height:416px;background:var(--grey-card);text-align:center}
.card .icon{width:86px;height:86px;border-radius:50%;background:var(--orange);margin:27px auto 0;display:flex;align-items:center;justify-content:center}
.card h3{color:var(--orange);font-size:24px;font-weight:600;margin-top:20px}
.card p{font-size:21px;line-height:29px;margin:14px 36px 0}
.pill{display:inline-block;background:var(--orange);color:var(--white);font-size:17px;font-weight:500;border-radius:16px;padding:1px 16px;margin-top:30px}
/* about */
.about{left:0;top:1413px;width:1200px;height:559px;background:linear-gradient(100deg,#14163a 0%,#1b1240 55%,#241a4e 100%)}
.about-photo{left:650px;top:1350px;width:450px;height:622px;background:linear-gradient(180deg,#5a3c2c 0%,#cdb8a0 35%,#6b4a3c 70%,#3a3a40 100%);border-radius:160px 160px 0 0}
.about-title{left:160px;top:1487px;color:var(--white);font-size:42px;font-weight:700}
.about-text{left:155px;top:1570px;width:480px;color:var(--white);font-size:21px;line-height:29px;font-weight:500}
.about-btn{left:157px;top:1816px;width:160px;height:40px;border-radius:20px}
/* projects */
.projects-title{left:93px;top:2018px;font-size:44px}
.projects-text{left:98px;top:2098px;width:560px;font-size:21px;line-height:29px}
.tab-active{left:90px;top:2224px;width:260px;height:38px;border-radius:6px;background:var(--orange);color:var(--white);font-size:21px;font-weight:600;display:flex;align-items:center;justify-content:center}
.tab{left:102px;font-size:21px;font-weight:600}
.tab-line-o{left:351px;top:2300px;width:3px;height:170px;background:var(--orange)}
.tab-line-b{left:351px;top:2470px;width:3px;height:115px;background:var(--line-blue)}
.project-visual{left:433px;top:2200px;width:680px;height:417px;border-radius:90px 0 100px 0;background:radial-gradient(circle at 60% 30%,#3f6fb0 0%,#1a3f7a 45%,#0b2350 100%)}
.project-head{left:480px;top:2385px;color:var(--white);font-size:26px;font-weight:700}
.project-text{left:480px;top:2436px;width:420px;color:var(--white);font-size:21px;line-height:29px}
.project-btn{left:482px;top:2542px;width:184px;height:46px;background:var(--orange);color:var(--white);font-size:24px;font-weight:600;display:flex;align-items:center;justify-content:center}
/* contact */
.contact{left:0;top:2617px;width:1200px;height:481px;background:var(--contact-bg)}
.contact-title{left:220px;top:2710px;font-size:44px}
.c-item{display:flex;gap:10px;font-size:19px;line-height:27px;align-items:flex-start}
.social{display:flex;gap:11px}
.social span{width:32px;height:32px;border-radius:50%;display:block;background:var(--orange)}
.field{left:601px;width:397px;background:var(--white);border:1px solid #d8d8d8;font-size:18px;color:#777;padding:8px 16px}
.submit{left:601px;top:2967px;width:397px;height:46px;background:var(--orange);color:var(--white);font-size:21px;font-weight:600;display:flex;align-items:center;justify-content:center}
/* footer */
.foot-brand{left:80px;top:3212px;font-size:25px;font-weight:700;color:var(--orange)}
.foot-head{top:3175px;font-size:21px;font-weight:500;color:var(--orange)}
.foot-list{top:3233px;list-style:none;font-size:21px;line-height:34px}
.foot-list li::before{content:"›";color:var(--orange);margin-right:8px}
.foot-rule{left:0;top:3412px;width:1200px;height:1px;background:#999}
.copy{left:0;top:3424px;width:1200px;text-align:center;font-size:18px;font-weight:500}
</style>
</head>
<body>
<header class="site-header abs"></header>
<div class="brand abs"><span class="dot"></span>CopperWren</div>
<nav class="nav abs">
  <a class="active">HOME</a><a>ABOUT US</a><a>PRODUCTS</a><a>PROJECTS</a><a>CONTRIBUTIONS</a><a>NEWS</a><a>PRIVACY</a>
</nav>

<section class="hero abs" role="img" aria-label="Office worker relaxing by a large window overlooking a city"></section>
<h1 class="hero-title abs">LOREM IPSUM DOLOR SIT<br>AMET, IPSUM DOLOR</h1>
<p class="hero-text abs">Lorem ipsum dolor sit amet, consectetur adipiscing elit, sed do eiusmod . Risus commodo viverra maecenas accumsan lacus vel facilisis.</p>
<div class="hero-btn btn-outline abs">Read More</div>

<h2 class="products-title section-title abs">OUR PRODUCTS</h2>
<div class="card abs" style="left:87px">
  <div class="icon"><svg width="44" height="44" viewBox="0 0 44 44" fill="none" stroke="#fff" stroke-width="2.5"><circle cx="20" cy="20" r="15"/><path d="M5 20h30M20 5c-6 6-6 24 0 30M20 5c6 6 6 24 0 30"/></svg></div>
  <h3>COPPERWREN</h3><p>Lorem ipsum dolor sit amet, consectetur adipiscing elit, sed do eiusmod tempor</p><span class="pill">Read More</span>
</div>
<div class="card abs" style="left:444px">
  <div class="icon"><svg width="44" height="44" viewBox="0 0 44 44" fill="none" stroke="#fff" stroke-width="2.5"><circle cx="18" cy="18" r="6"/><circle cx="29" cy="14" r="4"/><path d="M10 38V28a14 14 0 1 1 22-4l2 6h-4v6"/></svg></div>
  <h3>COPPERWREN</h3><p>Lorem ipsum dolor sit amet, consectetur adipiscing elit, sed do eiusmod tempor</p><span class="pill">Read More</span>
</div>
<div class="card abs" style="left:800px">
  <div class="icon"><svg width="44" height="44" viewBox="0 0 44 44" fill="none" stroke="#fff" stroke-width="2.5"><circle cx="22" cy="18" r="3"/><path d="M22 21l-5 17M22 21l5 17M14 10a11 11 0 0 0 0 16M30 10a11 11 0 0 1 0 16M9 5a18 18 0 0 0 0 26M35 5a18 18 0 0 1 0 26"/></svg></div>
  <h3>COPPERWREN</h3><p>Lorem ipsum dolor sit amet, consectetur adipiscing elit, sed do eiusmod tempor</p><span class="pill">Read More</span>
</div>

<section class="about abs" role="img" aria-label="Dark background of blurred code on a screen"></section>
<div class="about-photo abs" role="img" aria-label="Young man with headphones working on a laptop"></div>
<h2 class="about-title abs">ABOUT US</h2>
<p class="about-text abs">Lorem ipsum dolor sit amet, consectetur adipiscing elit, sed do eiusmod tempor incididunt ut labore et dolore magna aliqua. Quis ipsum suspendisse ultrices gravida. Risus commodo viverra maecenas accumsan lacus vel facilisis. ommodo viverra maecenas accumsan lacus vel facilisis.</p>
<div class="about-btn btn-outline abs">Read More</div>

<h2 class="projects-title section-title abs">Current Projects</h2>
<p class="projects-text abs">Lorem ipsum dolor sit amet, consectetur adipiscing elit, sed do eiusmod tempor inci labore et dolore</p>
<div class="tab-active abs">Artificial Intelligenece</div>
<div class="tab abs" style="top:2296px">Extended Reality</div>
<div class="tab abs" style="top:2365px">Data Visualization</div>
<div class="tab abs" style="top:2425px">Artificial Intelligenece</div>
<div class="tab abs" style="top:2493px">Current Projects</div>
<div class="tab abs" style="top:2561px">Extended Reality</div>
<div class="tab-line-o abs"></div><div class="tab-line-b abs"></div>
<div class="project-visual abs" role="img" aria-label="Blue network of connected points with a robotic hand"></div>
<h3 class="project-head abs">ARTIFICIAL INTELIGENCE</h3>
<p class="project-text abs">Lorem ipsum dolor sit amet, consectetur adipiscing elit, sed do eiusmod tempor incididunt ut labore</p>
<div class="project-btn abs">READ MORE</div>

<section class="contact abs"></section>
<h2 class="contact-title section-title abs">Contact us</h2>
<div class="c-item abs" style="left:220px;top:2788px"><svg width="20" height="24" viewBox="0 0 20 24"><path d="M4 2l4 5-2 3c1 4 4 7 7 9l3-2 4 4-3 3C8 23 1 12 2 4z" fill="#ff8a00"/></svg>555-010-2048</div>
<div class="c-item abs" style="left:220px;top:2840px"><svg width="22" height="22" viewBox="0 0 22 22"><rect x="1" y="5" width="20" height="14" fill="#ff8a00"/><path d="M1 5l10 8 10-8" stroke="#fff" stroke-width="1.5" fill="none"/></svg>@infocopperwren.com</div>
<div class="c-item abs" style="left:220px;top:2892px"><svg width="20" height="26" viewBox="0 0 20 26"><path d="M10 1a9 9 0 0 1 9 9c0 7-9 15-9 15S1 17 1 10a9 9 0 0 1 9-9z" fill="#ff8a00"/><circle cx="10" cy="10" r="3.5" fill="#fff"/></svg><span>Lorem ipsum dolor sit amet,<br>consectetur &nbsp;dolor sit amet</span></div>
<div class="social abs" style="left:222px;top:2964px"><span></span><span></span><span></span></div>
<div class="field abs" style="top:2719px;height:48px">Enter your name</div>
<div class="field abs" style="top:2787px;height:48px">Enter your email</div>
<div class="field abs" style="top:2855px;height:90px">Message</div>
<div class="submit abs">Submit</div>

<div class="foot-brand abs">CopperWren</div>
<div class="social abs" style="left:101px;top:3272px"><span style="width:24px;height:24px"></span><span style="width:24px;height:24px"></span><span style="width:24px;height:24px"></span></div>
<div class="foot-head abs" style="left:275px">Quick Links</div>
<ul class="foot-list abs" style="left:278px"><li>Home</li><li>About us</li><li>Products</li><li>Projects</li></ul>
<div class="foot-head abs" style="left:527px">Information</div>
<ul class="foot-list abs" style="left:529px"><li>Terms &amp; Condition</li><li>Privacy Policy</li><li>About Us</li><li>Support</li></ul>
<div class="foot-head abs" style="left:820px">Contact Us</div>
<div class="c-item abs" style="left:822px;top:3236px"><svg width="20" height="24" viewBox="0 0 20 24"><path d="M4 2l4 5-2 3c1 4 4 7 7 9l3-2 4 4-3 3C8 23 1 12 2 4z" fill="#ff8a00"/></svg>555-010-2048</div>
<div class="c-item abs" style="left:822px;top:3270px"><svg width="22" height="22" viewBox="0 0 22 22"><rect x="1" y="5" width="20" height="14" fill="#ff8a00"/><path d="M1 5l10 8 10-8" stroke="#fff" stroke-width="1.5" fill="none"/></svg>@infocopperwren.com</div>
<div class="c-item abs" style="left:822px;top:3305px"><svg width="20" height="26" viewBox="0 0 20 26"><path d="M10 1a9 9 0 0 1 9 9c0 7-9 15-9 15S1 17 1 10a9 9 0 0 1 9-9z" fill="#ff8a00"/><circle cx="10" cy="10" r="3.5" fill="#fff"/></svg><span>Lorem ipsum dolor sit amet,<br>consectetur &nbsp;dolor sit amet</span></div>
<div class="foot-rule abs"></div>
<p class="copy abs">All rights reserved.Copyrights @ 2023</p>
</body>
</html>
```